SnackHarbor!!! A Vending Machine Business Looking for an attractive website.

We are a vending machine business in Northern Michigan. We have changed our name and have rebranded our company. We would like an attractive website that shares who we are, what services we provide, the products we offer in our machines, along with a form businesses can fill out to see if they are a good fit for our company. I would like to have a Home Page, About SnackHarbor, Why Choose SnackHarbor?, Products & Services, Contact Us (With a Login Option), and a page with a questionnaire for thos interested in getting a FREE Vending Machine.

Target Market(s)

Businesses, Campgrounds, Schools, and many more in Northern Michigan

Industry/Entity Type

Vending Machines

Number of Pages Required

5+ page

Requirements
Must have
• An inviting and enticing Home Page. I want to get my potential clients engaged in our website.
Nice to have
• Possibly background photos from Northern Michigan
Should not have
• A corporate feel. I do not want a boring website.

```html
<!DOCTYPE html>
<html lang="en">
<head>
<meta charset="utf-8">
<title>SnackHarbor — Elevating Snacking One Vend at a Time</title>
<link href="https://fonts.googleapis.com/css2?family=Fraunces:opsz,wght@9..144,900&family=Figtree:wght@400;500;600;700&display=swap" rel="stylesheet">
<style>
:root{
  --cream:#f4f1e6;
  --cream-deep:#e6e2d3;
  --navy:#1c1c4c;
  --green:#2d5a27;
  --white:#ffffff;
  --line:#c9c6bb;
  --ink:#1c1c2c;
}
*{box-sizing:border-box;margin:0;padding:0}
html,body{width:1200px;height:4077px;overflow:hidden;background:var(--white)}
body{position:relative;font-family:"Figtree",sans-serif;color:var(--ink)}
.abs{position:absolute}
.display{font-family:"Fraunces",serif;font-weight:900;line-height:1.05;letter-spacing:-.5px}
.green{color:var(--green)}
.navy{color:var(--navy)}

/* header */
.hero-bg{left:0;top:0;width:1200px;height:600px}
.brand{font-family:"Fraunces",serif;font-weight:900;color:var(--navy);display:flex;align-items:center;gap:8px}
.brand .mark{width:14px;height:14px;background:var(--green)}
.nav{display:flex;align-items:center;background:var(--white);border-radius:30px;padding:3px;font-weight:600;font-size:14px;color:var(--navy)}
.nav a{color:inherit;text-decoration:none;padding:0 26px;height:42px;display:flex;align-items:center;border-radius:30px}
.nav a.active{background:var(--navy);color:var(--white)}

.tagline{left:0;width:1200px;top:138px;text-align:center;font-family:"Fraunces",serif;font-weight:900;font-size:16px;letter-spacing:14px;color:var(--navy)}
.hero-title{left:0;width:1200px;top:166px;text-align:center;font-size:64px}
.hero-photo{left:309px;top:337px;width:582px;height:257px;background:linear-gradient(90deg,#1b1b1b,#3a2e22 30%,#252525 50%,#2e3d4a 75%,#1b1b1b)}

/* about */
.about-title{left:180px;top:722px;font-size:60px;color:var(--green)}
.about-text{left:180px;top:880px;width:385px;font-size:15px;line-height:22.5px;font-weight:500}
.about-text p+p{margin-top:14px}
.about-panel{left:595px;top:692px;width:450px;height:432px;background:var(--cream);border-radius:48px}
.about-photo{left:646px;top:692px;width:399px;height:400px;border-radius:48px;background:linear-gradient(180deg,#5f86c9 0%,#a5c0e3 38%,#7d8b6c 52%,#2d6fa8 70%,#1f5b94 100%)}
.badge{left:559px;top:690px;width:108px;height:108px;border-radius:50%;background:var(--white);border:2px solid var(--navy)}

/* why */
.why-panel{left:100px;top:1208px;width:999px;height:742px;background:var(--cream);border-radius:95px}
.why-title{font-size:60px}
.why-ornament{left:948px;top:1302px;width:30px;height:94px;border-radius:15px;background:var(--cream-deep)}
.acc-item{left:253px;width:716px;border-bottom:1px solid var(--line)}
.acc-head{font-family:"Fraunces",serif;font-weight:900;font-size:22px;color:var(--navy);display:flex;justify-content:space-between;align-items:center}
.acc-icon{width:26px;height:26px;border-radius:50%;background:var(--green);position:relative}
.acc-icon::before,.acc-icon.plus::after{content:"";position:absolute;background:var(--white);left:7px;top:12px;width:12px;height:2px}
.acc-icon.plus::after{transform:rotate(90deg)}
.acc-body{font-size:15px;line-height:22.5px;font-weight:500;margin-top:18px;width:630px}

/* products */
.prod-title{left:0;width:1200px;top:2012px;text-align:center;font-size:62px}
.prod-text{left:340px;width:520px;top:2160px;text-align:center;font-size:15px;line-height:22.5px;font-weight:500}
.card{top:2275px;width:234px;height:394px;border-radius:40px;background:var(--cream);border:2px solid var(--green);overflow:hidden;text-align:center}
.card.navy-b{border-color:var(--navy)}
.card-photo{height:204px}
.card h3{font-family:"Fraunces",serif;font-weight:900;font-size:22px;margin-top:20px}
.card ul{list-style:none;margin-top:12px;font-weight:600;font-size:15px;line-height:27px}
.card li::before{content:"• "}

/* contact */
.contact-circle{left:122px;top:2800px;width:358px;height:358px;border-radius:50%;background:var(--cream)}
.contact-photo{left:201px;top:2770px;width:348px;height:417px;background:linear-gradient(90deg,#2a2a2a 0%,#444 40%,#1f4f9e 60%,#3a6fc0 100%);clip-path:polygon(0 0,42% 0,42% 21%,100% 21%,100% 100%,42% 100%,42% 76%,0 76%)}
.contact-title{left:602px;top:2778px;font-size:60px}
.contact-text{left:602px;top:2912px;width:420px;font-size:15px;line-height:22.5px;font-weight:500}
.field{height:44px;border-radius:22px;background:var(--cream);font-size:14px;font-weight:600;color:var(--navy);padding-left:18px;display:flex;align-items:center}
.btn{height:44px;border-radius:22px;display:flex;align-items:center;justify-content:center;font-size:14px;font-weight:700}
.btn-solid{background:var(--navy);color:var(--white)}
.btn-outline{border:2px solid var(--green);color:var(--navy)}

/* cta */
.cta-panel{left:100px;top:3293px;width:999px;height:411px;background:var(--cream);border-radius:70px}
.cta-title{left:0;width:1200px;top:3352px;text-align:center;font-size:62px;line-height:69px}
.cta-pill{left:366px;top:3581px;width:465px;height:60px;border-radius:30px;background:var(--white);display:flex;align-items:center;justify-content:space-between;padding:0 8px 0 18px;font-size:15px;font-weight:500}
.cta-pill .btn{height:44px;padding:0 26px;background:var(--navy);color:var(--white)}

/* footer */
.footer-rule{left:100px;top:3786px;width:999px;height:3px;background:var(--green)}
.footer-nav{left:348px;top:3969px;background:var(--cream)}
.copyright{left:0;width:1200px;top:4038px;text-align:center;font-size:14px;font-weight:600;color:var(--navy)}
</style>
</head>
<body>

<!-- hero -->
<svg class="abs hero-bg" viewBox="0 0 1200 600" aria-hidden="true">
  <path d="M0 0H1200V451Q600 740 0 451Z" fill="var(--cream)"/>
</svg>

<div class="abs brand" style="left:101px;top:24px;font-size:30px"><span class="mark"></span>SnackHarbor</div>
<nav class="abs nav" style="left:575px;top:19px">
  <a class="active">Home</a><a>About us</a><a>Why us</a><a>Product</a><a>Contact</a>
</nav>

<div class="abs tagline">CRAVE ✧ VEND ✧ REPEAT</div>
<h1 class="abs display hero-title"><span class="green">Elevating Snacking</span><br><span class="navy">One Vend at a Time</span></h1>
<div class="abs hero-photo" role="img" aria-label="Two stocked vending machines with snacks and drinks"></div>
<svg class="abs" style="left:0;top:440px" width="1200" height="160" viewBox="0 440 1200 160" aria-hidden="true">
  <path d="M0 451Q600 740 1200 451V600H0Z" fill="var(--white)"/>
  <path d="M0 451Q600 740 1200 451" fill="none" stroke="var(--green)" stroke-width="3"/>
</svg>

<!-- about -->
<h2 class="abs display about-title">About<br>SnackHarbor</h2>
<div class="abs about-text">
  <p>At SnackHarbor, we don't just vend snacks—we curate cravings. Our customized vending solutions bring flavor, convenience, and community to Northern Michigan.</p>
  <p>Whether you're reaching for a mid-morning snack, a refreshing beverage, or a satisfying breakfast burrito, SnackHarbor delivers delight with every bite.</p>
</div>
<div class="abs about-panel"></div>
<div class="abs about-photo" role="img" aria-label="Aerial view of a Northern Michigan harbor town with a marina"></div>
<div class="abs badge" role="img" aria-label="Northern Michigan badge"></div>

<!-- why -->
<div class="abs why-panel"></div>
<h2 class="abs display why-title navy" style="left:185px;top:1276px">Why Choose</h2>
<h2 class="abs display why-title green" style="left:248px;top:1343px">SnackHarbor?</h2>
<div class="abs why-ornament" role="img" aria-label="Hand-drawn wavy arrow pointing down"></div>

<div class="abs acc-item" style="top:1452px;height:156px">
  <div class="acc-head">1. Local Love<span class="acc-icon"></span></div>
  <p class="acc-body">We celebrate the heart of Michigan by partnering with local legends. Say hello to Pine Ridge Jerky and Lakeshore Potato Chips—our hometown heroes. Their flavors dance on your taste buds, and we're thrilled to bring them straight to your workplace.</p>
</div>
<div class="abs acc-item" style="top:1636px;height:55px"><div class="acc-head">2. Unleash Your Cravings<span class="acc-icon plus"></span></div></div>
<div class="abs acc-item" style="top:1716px;height:55px"><div class="acc-head">3. Quality Meets Convenience<span class="acc-icon plus"></span></div></div>
<div class="abs acc-item" style="top:1797px;height:55px"><div class="acc-head">4. Pandemic-Proof &amp; Recession-Ready<span class="acc-icon plus"></span></div></div>

<!-- products -->
<h2 class="abs display prod-title"><span class="green">Take Look</span><br><span class="navy">Our Products</span></h2>
<p class="abs prod-text">When it comes to healthy options, our machines can't be beat! We have a large selection of products to choose from.Our machines are fully customized to suit the needs of each location.</p>

<div class="abs card" style="left:100px">
  <div class="card-photo" role="img" aria-label="Vending machine shelves full of snacks" style="background:linear-gradient(180deg,#2b2f3a,#6a4a3e 50%,#2a2d36)"></div>
  <h3 class="green">Beverages</h3>
  <ul class="navy"><li>Waters</li><li>Speciality waters</li><li>Juices</li><li>Sodas</li></ul>
</div>
<div class="abs card navy-b" style="left:355px">
  <div class="card-photo" role="img" aria-label="Bags of baked chips on a shelf" style="background:linear-gradient(180deg,#8a6a3a,#d4a24a 45%,#6b5530)"></div>
  <h3 class="navy">Snacks</h3>
  <ul class="green"><li>Baked Crackers</li><li>Baked Chips</li><li>Mixes</li><li>Crackers</li></ul>
</div>
<div class="abs card" style="left:609px">
  <div class="card-photo" role="img" aria-label="Pile of assorted candy bars" style="background:linear-gradient(135deg,#8a2a22,#c9482e 40%,#3b3f86 70%,#a63628)"></div>
  <h3 class="green">Bars</h3>
  <ul class="navy"><li>Gluten-Free Cookies</li><li>Snack Bars</li><li>Cookies</li><li>Childhood Memories</li></ul>
</div>
<div class="abs card navy-b" style="left:864px">
  <div class="card-photo" role="img" aria-label="Yogurt cups on a table" style="background:linear-gradient(90deg,#5a5a4e,#e8e2c0 45%,#cfd9a8 70%,#4a4a40)"></div>
  <h3 class="navy">Others</h3>
  <ul class="green"><li>Proteins</li><li>Breakfast Bites</li><li>No Time for Lunch</li><li>Yogurt</li></ul>
</div>

<!-- contact -->
<div class="abs contact-circle"></div>
<div class="abs contact-photo" role="img" aria-label="Snack vending machine beside a blue combo vending machine"></div>
<h2 class="abs display contact-title"><span class="green">Get</span><br><span class="navy">In Touch</span></h2>
<p class="abs contact-text">At SnackHarbor, we don't just vend snacks—we curate cravings. Our customized</p>
<div class="abs field" style="left:602px;top:2973px;width:228px">Full name</div>
<div class="abs field" style="left:839px;top:2973px;width:228px">Email</div>
<div class="abs field" style="left:602px;top:3028px;width:465px">Message</div>
<div class="abs btn btn-solid" style="left:602px;top:3082px;width:465px">Submit</div>
<div class="abs btn btn-outline" style="left:602px;top:3137px;width:465px">Login</div>

<!-- cta -->
<div class="abs cta-panel"></div>
<h2 class="abs display cta-title"><span class="green">Does Your Business</span><br><span class="navy">Need A Free Vending<br>Machine?</span></h2>
<div class="abs cta-pill">Please fill the questionare.<span class="btn">Yes, I want to fill it in</span></div>

<!-- footer -->
<div class="abs footer-rule"></div>
<div class="abs brand" style="left:0;width:1200px;justify-content:center;top:3846px;font-size:64px"><span class="mark" style="width:22px;height:22px"></span>SnackHarbor</div>
<nav class="abs nav footer-nav">
  <a class="active">Home</a><a>About us</a><a>Why us</a><a>Product</a><a>Contact</a>
</nav>
<p class="abs copyright">Copyright © 2024 SnackHarbor</p>

</body>
</html>
```